依頼概要
■ 依頼の目的/概要

弊社は「カード選びナビ広場 http://www.hoshizora-cardnavi.com/ 」というクレジットカードの比較サイトを運営しています。
今回はこのカード選びナビ広場のトップページのサイトデザインリニューアルをお願いします。

現在、サイト内( http://www.hoshizora-cardnavi.com/ )にある素材は自由に使って頂いて構いません。
既存のデザインを残しつつデザインをしていただいても
逆に完全新規にデザインをしていただいても構いません。
最終的なクオリティが高ければOKです。
素材サイトで何か素材を購入すればよりクオリティが高くなるのであれば
別途素材の購入も検討します。
その際はメッセージでご連絡ください。

■コーディング不要
コーディングは不要なので、デザインのみでOKです。

■ 希望するウェブデザイン

サイト訪問者が楽しくクレジットカードを選んだり
クレジットカードについての知識を学んだりできるようなデザインが希望です。
逆にサイト訪問者が堅苦しく感じてしまうようなデザインは避けたいです。
既存サイトでは下記URLのようなサイトデザインが好みです。

http://www.mz.tobira-net.com/mobile/index.html?bid=mz_gn_0007
http://www.mirumart.co.jp/kuruma/index.html?ca=top_glo_009
http://store.fenlow.com/jp/
http://store.tavix.jp/Special/Compare/Computer/Relmo/index.html

また「クレジットカード」で検索して1ページ目に出てくるサイトには
綺麗なサイトが多いので、こちらも参考にして頂きたいです。

【サイズの横幅について】

現在の横幅はぴったり950pxですが、
980px前後までであれば、横幅が大きくなっても構いません。
横幅が現在よりも小さくなるのは不可です。

ただし、ヘッダー部分とフッター部分は下記サイトのように横全体に広がっているデザインが希望です。
http://www.qrt.co.jp/ordercard/index.html

■ 納品ファイルの希望

第一希望 フォトショップ形式 + BMP形式
第二希望 イラストレーター形式 + BMP形式

■ 進め方

弊社の希望するイメージに近い提案を1つ(場合によって複数)選択させて頂きます。希望に近づけるために、修正要望を個別にさせて頂くこともあります。コンペ方式のため、修正後に当選されない場合も、どうかご了承ください。

■ その他/注意点

選択させて頂いたウェブデザインの著作権(財産権)等の扱いはTezukuri利用規約に従い、弊社に譲渡をお願いします。フォントや画像素材などを利用する場合は上記利用用途に使用できることを確認し、第三者の知的財産権等に注意して下さい。
■リニューアルによる変更点
今回のリニューアルではデザイン面だけでなくシステム面も強化するため
トップページのデザインが一部変更になります。
変更点は添付ファイルにまとめました。
なので現在のトップページのデザイン( http://www.hoshizora-cardnavi.com/
ではなく添付ファイル内のデザインを元にデザインをしてください。

```html
<!DOCTYPE html>
<html lang="ja">
<head>
<meta charset="utf-8">
<title>カード選びナビ広場 | お得なクレジットカードを探そう</title>
<link href="https://fonts.googleapis.com/css2?family=Noto+Sans+JP:wght@400;700&display=swap" rel="stylesheet">
<style>
:root{
  --blue:#1a6fc4;
  --blue-dark:#0b4f9a;
  --blue-light:#e6f2fb;
  --blue-line:#b9d6ee;
  --orange:#f39a1e;
  --orange-dark:#d97c06;
  --yellow:#fff5b8;
  --red:#d33;
  --text:#333;
  --muted:#777;
  --white:#fff;
  --bg:#f4f9fd;
}
*{box-sizing:border-box;margin:0;padding:0}
html,body{width:1200px;height:3688px;overflow:hidden}
body{font-family:"Noto Sans JP",sans-serif;color:var(--text);font-size:13px;background:var(--white);line-height:1.5;display:flex;flex-direction:column}
.header{height:112px;flex:none;background:linear-gradient(#fff,#eef6fc);border-bottom:1px solid var(--blue-line)}
.wrap{width:1160px;margin:0 auto;position:relative}
.header .wrap{display:flex;align-items:center;height:112px;gap:24px}
.site-name{display:flex;align-items:center;gap:10px;font-size:30px;font-weight:700;color:var(--blue);white-space:nowrap}
.site-name i{width:26px;height:26px;background:var(--orange);border-radius:50%}
.tagline{border-left:2px solid var(--blue-line);padding-left:18px;font-size:14px;color:var(--muted)}
.tagline b{display:block;font-size:22px;color:var(--blue-dark)}
.search-box{margin-left:auto;display:flex;gap:6px;align-self:flex-start;margin-top:18px}
.search-box span{width:200px;height:26px;border:1px solid var(--blue-line);background:#fff}
.search-box em{font-style:normal;background:var(--blue);color:#fff;padding:3px 12px;font-size:12px}
.gnav{height:40px;flex:none;background:linear-gradient(var(--blue),var(--blue-dark))}
.gnav ul{display:flex;list-style:none;height:40px;width:1160px;margin:0 auto}
.gnav li{flex:1;color:#fff;font-weight:700;font-size:15px;text-align:center;line-height:40px;border-right:1px solid rgba(255,255,255,.35)}
.gnav li:first-child{background:#0a3f7d}
.page{flex:1;display:flex;gap:30px;width:1160px;margin:8px auto 0;min-height:0}
.main{width:780px;display:flex;flex-direction:column;padding-bottom:24px}
.side{width:350px}
.intro{height:340px;flex:none;display:flex;background:linear-gradient(#fff,var(--blue-light));border:1px solid var(--blue-line);padding:26px 24px}
.intro-text{width:440px}
.intro-text p{font-size:13px;line-height:2}
.intro-text p strong{color:var(--red)}
.news{margin-top:18px;list-style:none}
.news li{font-size:12px;border-bottom:1px dotted var(--blue-line);padding:4px 0}
.news li span{display:inline-block;background:var(--blue);color:#fff;font-size:11px;padding:0 6px;margin-right:8px}
.news li a{color:var(--blue)}
.intro-art{flex:1;margin-left:20px;background:linear-gradient(135deg,#fdeee2,#cfe4f6 60%,#a9cbe9);border-radius:8px}
.sec-title{height:50px;display:flex;align-items:center;padding-left:16px;font-size:22px;font-weight:700;color:var(--blue-dark);background:linear-gradient(#fff,var(--blue-light));border-left:8px solid var(--blue);border-bottom:2px solid var(--blue)}
.sec-title small{font-size:16px;color:var(--orange-dark);margin-right:12px}
.popular{margin-top:18px;flex:none}
.popular-grid{display:grid;grid-template-columns:repeat(4,1fr);gap:10px;margin-top:10px}
.fee{text-align:center;font-size:12px}
.fee h3{background:var(--blue);color:#fff;font-size:14px;padding:4px 0}
.fee h3 b{color:var(--yellow)}
.fee .name{color:var(--blue);font-weight:700;margin-top:8px}
.card{height:110px;margin:8px 14px 0;border-radius:8px;background:linear-gradient(135deg,#cfd8e2,#8ea7c2)}
.card.gold{background:linear-gradient(135deg,#f2e1a8,#c9a24a)}
.card.blue{background:linear-gradient(135deg,#a8cff0,#2f77c0)}
.card.red{background:linear-gradient(135deg,#f6c2c2,#d0404c)}
.card.sm{height:60px;margin:0}
.fee p{text-align:left;padding:6px 10px;color:var(--muted);font-size:11px;line-height:1.6}
.feature{margin-top:22px;flex:none}
.pickup{margin-top:12px;border:1px solid var(--blue-line);padding:14px 16px}
.pickup h4{font-size:14px;color:var(--blue-dark);border-bottom:1px dotted var(--blue-line);padding-bottom:6px}
.pickup-grid{display:grid;grid-template-columns:repeat(5,1fr);gap:18px 14px;margin-top:14px}
.thumb{font-size:11px;color:var(--blue)}
.thumb div{height:170px;border:1px solid var(--blue-line);background:linear-gradient(#eaf3fb,#bcd6ee)}
.thumb p{margin-top:6px;line-height:1.5;height:34px}
.more{text-align:right;font-size:11px;color:var(--blue);margin-top:10px}
.filter{margin-top:22px;flex:none}
.filter-body{border:1px solid var(--blue-line);padding:16px 20px 22px}
.group{margin-bottom:26px}
.group h4{font-size:14px;color:var(--blue-dark);padding:5px 0 5px 10px;border-left:4px solid var(--orange);background:var(--bg);margin-bottom:12px}
.checks{display:grid;grid-template-columns:repeat(4,1fr);row-gap:20px;font-size:12px;padding-left:10px}
.checks span::before{content:"";display:inline-block;width:11px;height:11px;border:1px solid #999;margin-right:6px;vertical-align:-1px;background:#fff}
.select{width:220px;height:26px;border:1px solid #aaa;margin-left:10px;font-size:12px;padding:3px 8px}
.result{text-align:center;margin-top:24px;font-size:14px}
.result b{font-size:38px;color:var(--orange-dark);margin:0 4px}
.btn{display:block;width:280px;margin:12px auto 0;background:linear-gradient(var(--orange),var(--orange-dark));color:#fff;text-align:center;font-weight:700;font-size:16px;padding:10px 0;border-radius:22px}
.battle{margin-top:22px;flex:1;display:flex;flex-direction:column}
.battle-grid{flex:1;display:grid;grid-template-columns:1fr 1fr;grid-template-rows:1fr 1fr;gap:18px;margin-top:14px}
.match{border:1px solid var(--blue-line);background:var(--bg);padding:0 0 22px;text-align:center;display:flex;flex-direction:column}
.match h4{background:linear-gradient(#fff,var(--blue-light));color:var(--blue-dark);font-size:15px;padding:8px;border-bottom:1px solid var(--blue-line)}
.versus{flex:1;display:flex;align-items:center;justify-content:center;gap:18px;padding:20px}
.versus .card{width:140px;height:90px;margin:0}
.versus b{font-size:26px;color:var(--red)}
.match .btn{width:170px;font-size:14px;padding:7px 0;margin-top:0}
.note{font-size:11px;color:var(--blue);text-align:center;margin-top:14px}
.side-box{border:1px solid var(--blue-line);margin-bottom:14px}
.ad{height:220px;display:flex;flex-direction:column;align-items:center;justify-content:center;background:linear-gradient(#fff,#fce9d5);text-align:center;gap:6px}
.ad .brand{font-size:28px;font-weight:700;color:var(--blue-dark)}
.ad p{font-size:13px}
.ad p b{color:var(--red);font-size:18px}
.side-title{background:linear-gradient(var(--blue),var(--blue-dark));color:#fff;font-weight:700;padding:8px 12px;font-size:14px}
.cat{padding:14px}
.cat-head{height:40px;background:linear-gradient(90deg,#fef5d6,#fff);color:var(--orange-dark);font-weight:700;line-height:40px;padding-left:12px}
.cat ul{list-style:none;margin-top:8px}
.cat li{font-size:13px;padding:6px 0 6px 18px;border-bottom:1px dotted var(--blue-line);position:relative}
.cat li::before{content:"";position:absolute;left:4px;top:12px;border:4px solid transparent;border-left:6px solid var(--blue)}
.emoney{display:grid;grid-template-columns:1fr 1fr;gap:10px;padding:14px}
.emoney span{height:60px;border:1px solid var(--blue-line);display:flex;align-items:center;justify-content:center;font-weight:700;font-size:18px;color:var(--blue-dark);background:#fff}
.ad2{height:180px;background:linear-gradient(#fff,#e6f2fb);display:flex;flex-direction:column;align-items:center;justify-content:center;gap:4px}
.ad2 .tag{background:var(--red);color:#fff;font-size:12px;padding:2px 10px}
.ad2 .pt b{color:var(--red);font-size:20px}
.ad2 .big{font-size:24px;font-weight:700;color:var(--blue-dark)}
.ad2 .btn{width:200px;font-size:14px;padding:6px 0;margin-top:6px}
.campaign{padding:12px}
.campaign-head{font-size:18px;font-weight:700;color:var(--red);text-align:center;padding:8px 0;background:var(--yellow)}
.camp{display:flex;gap:10px;padding:14px 0;border-bottom:1px dotted var(--blue-line)}
.camp .card{width:110px;flex:none}
.camp p{font-size:12px;line-height:1.6}
.camp p b{color:var(--blue)}
.camp p mark{background:var(--yellow)}
.ad3{height:250px;background:linear-gradient(#fff,#f6efd8);display:flex;flex-direction:column;align-items:center;justify-content:center;gap:10px}
.ad3 .card{width:200px;height:120px;margin:0}
.ad3 p{font-weight:700;color:#8a6a1a;font-size:16px}
.footer{flex:none;position:relative;width:1200px;height:188px}
.pagetop{position:absolute;right:20px;top:-20px;background:var(--blue-dark);color:#fff;font-size:11px;padding:2px 10px}
.footer-bottom{height:148px;background:var(--blue-dark);color:#dbe9f7}
.footer-bottom .wrap{display:flex;justify-content:space-between;padding-top:20px}
.footer-bottom p{font-size:11px;width:640px;line-height:1.8}
.footer-bottom .site-name{font-size:22px;color:#fff}
.copy{text-align:right;font-size:11px;padding:14px 20px 0}
</style>
</head>
<body>
<header class="header">
  <div class="wrap">
    <div class="site-name"><i></i>カード選びナビ広場</div>
    <div class="tagline">〈ライフスタイルに合わせた〉<b>お得なクレジットカードを探そう！</b></div>
    <div class="search-box"><span></span><em>検索</em></div>
  </div>
</header>
<nav class="gnav"><ul><li>カテゴリーから探す</li><li>一覧から絞り込み検索</li><li>一覧＋比較</li><li>ブログ</li><li>クレジットカードを知る・特集</li></ul></nav>

<div class="page">
  <main class="main">
    <section class="intro">
      <div class="intro-text">
        <p>クレジットカードにはさまざまなサービスがついています。よくサービスを比較し、<strong>自分のライフスタイルにあわせた</strong>クレジットカードを選ぶことでクレジットカードの<strong>メリットを最大限に</strong>活かすことができます。</p>
        <ul class="news">
          <li><span>新着情報</span></li>
          <li>2013年03月12日 <a>ポイント還元率の高いカードの特集を更新しました</a></li>
          <li>2013年03月05日 <a>年会費無料カードのランキングを更新しました</a></li>
          <li>2013年02月26日 <a>旅行保険付きカードの比較ページを追加しました</a></li>
          <li>2013年02月18日 <a>電子マネー対応カードの一覧を更新しました</a></li>
          <li>2013年02月08日 <a>学生向けカードの選び方を公開しました</a></li>
        </ul>
      </div>
      <div class="intro-art" role="img" aria-label="カードを手に案内する女性とクレジットカードのイラスト"></div>
    </section>

    <section class="popular">
      <h2 class="sec-title"><small>年会費別</small>当サイト人気クレジットカード</h2>
      <div class="popular-grid">
        <div class="fee"><h3>年会費 <b>無料</b></h3><div class="card blue" role="img" aria-label="クレジットカード券面"></div><div class="name">ナビカード</div><p>年会費無料でポイントがたまりやすい定番の一枚です。</p></div>
        <div class="fee"><h3><b>1円〜1,999円</b></h3><div class="card" role="img" aria-label="クレジットカード券面"></div><div class="name">ひろばカード</div><p>お手頃な年会費で旅行保険も付いた人気カードです。</p></div>
        <div class="fee"><h3><b>2,000円〜9,999円</b></h3><div class="card red" role="img" aria-label="クレジットカード券面"></div><div class="name">ステップカード</div><p>ショッピング保険と特典が充実したバランス型です。</p></div>
        <div class="fee"><h3><b>1万円以上</b></h3><div class="card gold" role="img" aria-label="ゴールドカード券面"></div><div class="name">プレミアゴールド</div><p>空港ラウンジなど上質なサービスが受けられます。</p></div>
      </div>
    </section>

    <section class="feature">
      <h2 class="sec-title">クレジットカードを知る・特集</h2>
      <div class="pickup">
        <h4>おすすめ記事をピックアップ</h4>
        <div class="pickup-grid">
          <div class="thumb"><div role="img" aria-label="記事の写真"></div><p>海外旅行に強いカードの選び方</p></div>
          <div class="thumb"><div role="img" aria-label="記事の写真"></div><p>空港ラウンジを使えるカード</p></div>
          <div class="thumb"><div role="img" aria-label="記事の写真"></div><p>はじめてのクレジットカード</p></div>
          <div class="thumb"><div role="img" aria-label="記事の写真"></div><p>安心のセキュリティ対策</p></div>
          <div class="thumb"><div role="img" aria-label="記事の写真"></div><p>ポイントを賢くためる方法</p></div>
          <div class="thumb"><div role="img" aria-label="記事の写真"></div><p>家族カードの上手な使い方</p></div>
          <div class="thumb"><div role="img" aria-label="記事の写真"></div><p>マイルがたまるカード特集</p></div>
          <div class="thumb"><div role="img" aria-label="記事の写真"></div><p>若葉マークの学生カード</p></div>
          <div class="thumb"><div role="img" aria-label="記事の写真"></div><p>不正利用から守る補償制度</p></div>
          <div class="thumb"><div role="img" aria-label="記事の写真"></div><p>リボ払いの仕組みと注意点</p></div>
        </div>
        <div class="more">▶ その他の記事を見る</div>
      </div>
    </section>

    <section class="filter">
      <h2 class="sec-title">クレジットカード一覧から絞り込み検索</h2>
      <div class="filter-body">
        <div class="group"><h4>サービス種類</h4><div class="checks">
          <span>ポイント還元率が高い</span><span>マイルがたまる</span><span>ショッピング保険</span><span>旅行保険が充実</span>
          <span>ETCカード発行</span><span>空港ラウンジ</span><span>キャッシング可能</span><span>即日発行</span>
          <span>ガソリン割引</span><span>学生向け</span><span>女性向け</span><span>年会費無料</span>
          <span>家族カード</span><span>審査がやさしい</span><span>ネット通販に強い</span><span>海外利用に強い</span></div></div>
        <div class="group"><h4>年会費</h4><div class="checks">
          <span>永年無料</span><span>初年度無料</span><span>条件付き無料</span><span>1円〜1,999円</span>
          <span>2,000円〜4,999円</span><span>5,000円〜9,999円</span><span>1万円〜2万円</span><span>2万円以上</span>
          <span>指定なし</span></div></div>
        <div class="group"><h4>付帯保険</h4><div class="checks">
          <span>海外旅行保険</span><span>国内旅行保険</span><span>ショッピング保険</span><span>自動付帯</span>
          <span>利用付帯</span><span>家族特約</span><span>航空便遅延</span><span>携行品損害</span>
          <span>指定なし</span></div></div>
        <div class="group"><h4>種類</h4><div class="checks">
          <span>一般カード</span><span>ゴールドカード</span><span>プラチナカード</span><span>法人カード</span>
          <span>提携カード</span><span>学生カード</span></div></div>
        <div class="group"><h4>電子マネー</h4><div class="checks">
          <span>Nimo</span><span>交通系カード</span><span>後払い型</span><span>チャージ型</span>
          <span>ポイント付与あり</span><span>スマホ対応</span><span>オートチャージ</span><span>指定なし</span>
          <span>その他</span></div></div>
        <div class="group"><h4>追加可能なカード</h4><div class="checks">
          <span>ETCカード</span><span>家族カード</span><span>予備カード</span><span>指定なし</span></div></div>
        <div class="group"><h4>カードブランド</h4><div class="select">▼ 選択してください</div></div>
        <div class="group"><h4>国際ブランド</h4><div class="checks">
          <span>Orbis</span><span>ブランドA</span><span>ブランドB</span><span>ブランドC</span>
          <span>ブランドD</span><span>指定なし</span></div></div>
        <div class="result">現在の条件で<b>67</b>枚のカードが該当します</div>
        <div class="btn">この条件で検索する</div>
      </div>
    </section>

    <section class="battle">
      <h2 class="sec-title">クレジットカード対決</h2>
      <div class="battle-grid">
        <div class="match"><h4>スタンダードカード対決</h4><div class="versus"><div class="card blue" role="img" aria-label="カード券面"></div><b>VS</b><div class="card" role="img" aria-label="カード券面"></div></div><div class="btn">比較する</div></div>
        <div class="match"><h4>コンビニでお得なクレジットカード対決</h4><div class="versus"><div class="card red" role="img" aria-label="カード券面"></div><b>VS</b><div class="card blue" role="img" aria-label="カード券面"></div></div><div class="btn">比較する</div></div>
        <div class="match"><h4>ゴールドカード対決</h4><div class="versus"><div class="card gold" role="img" aria-label="ゴールドカード券面"></div><b>VS</b><div class="card gold" role="img" aria-label="ゴールドカード券面"></div></div><div class="btn">比較する</div></div>
        <div class="match"><h4>ポイントがお得なクレジットカード対決</h4><div class="versus"><div class="card" role="img" aria-label="カード券面"></div><b>VS</b><div class="card red" role="img" aria-label="カード券面"></div></div><div class="btn">比較する</div></div>
      </div>
      <p class="note">▶ クレジットカード対決をもっと見る</p>
    </section>
  </main>

  <aside class="side">
    <div class="side-box ad"><div class="brand">Fresh Plus</div><p>入会後3ヶ月間ポイント<b>5倍</b></p><div class="card blue" style="width:160px;height:90px;margin:0" role="img" aria-label="カード券面"></div><p>最大<b>6,000円分</b>プレゼント</p></div>
    <div class="side-box"><div class="side-title">カテゴリーからカードを探す</div>
      <div class="cat"><div class="cat-head">あなたにぴったりの一枚を！</div><ul>
        <li>年会費無料のカード</li><li>ポイント還元率が高いカード</li><li>マイルがたまるカード</li><li>旅行保険が充実したカード</li><li>ゴールドカード</li><li>学生向けのカード</li><li>即日発行できるカード</li><li>ETCカードが作れるカード</li><li>女性に人気のカード</li></ul></div></div>
    <div class="side-box emoney"><span>Nimo</span><span>交通系</span><span>Orbis</span><span>後払い</span></div>
    <div class="side-box ad2"><span class="tag">年会費無料</span><div class="pt">ポイント<b>3倍</b></div><div>みなと銀河カード</div><div class="big">エブリワン</div><div class="btn">詳細はこちら ›</div></div>
    <div class="side-box"><div class="side-title">ライフアップキャンペーン情報</div>
      <div class="campaign"><div class="campaign-head">タイアップキャンペーン</div>
        <div class="camp"><div class="card sm blue" role="img" aria-label="カード券面"></div><p><b>ナビカード</b><br>入会で<mark>最大8,000円分</mark>のポイントをプレゼント中です。</p></div>
        <div class="camp"><div class="card sm gold" role="img" aria-label="カード券面"></div><p><b>プレミアゴールド</b><br>初年度年会費無料、<mark>空港ラウンジ</mark>も利用可能です。</p></div>
        <div class="camp"><div class="card sm red" role="img" aria-label="カード券面"></div><p><b>ステップカード</b><br>ネット申込限定で<mark>ポイント2倍</mark>キャンペーン実施中。</p></div>
        <div class="camp"><div class="card sm" role="img" aria-label="カード券面"></div><p><b>ひろばカード</b><br>期間中のご利用で<mark>3,000円</mark>キャッシュバック。</p></div>
        <div class="camp"><div class="card sm blue" role="img" aria-label="カード券面"></div><p><b>エブリワン</b><br>新規入会で<mark>最大5,000円分</mark>をプレゼントします。</p></div>
      </div></div>
    <div class="side-box ad3"><div class="card gold" role="img" aria-label="ゴールドカード券面"></div><p>Amberline Gold Card</p></div>
  </aside>
</div>

<footer class="footer">
  <div class="pagetop">▲ PAGETOP</div>
  <nav class="gnav"><ul><li>カテゴリーから探す</li><li>一覧から絞り込み検索</li><li>一覧＋比較</li><li>ブログ</li><li>クレジットカードを知る・特集</li></ul></nav>
  <div class="footer-bottom">
    <div class="wrap">
      <p>カード選びナビ広場について：当サイトは各社のクレジットカードの情報を比較し、ライフスタイルに合わせたカード選びをお手伝いするサイトです。掲載内容は各社の公式情報をもとにしていますが、最新の条件は必ず各社サイトでご確認ください。</p>
      <div class="site-name">カード選びナビ広場</div>
    </div>
    <div class="copy">Copyright © 2013 カード選びナビ広場 All Rights Reserved.</div>
  </div>
</footer>
</body>
</html>
```